Medical equipment business looking for professional, unique business card

We need a business card design for a durable medical equipment company. We are small but would like our cards to express that we are much bigger. We focus on braces (back, knee, wrist, etc) but also do crutches, rollators, wheelchairs- basically medical equipment that gets you going and back in Stride. Our colors are blue and green and our logo has an arrow and use of a "spine". We'd like to express professionalism while being unique.

Industry/Entity Type

Medical Equipment

Contact Information for Business Card

Professional feel but unique. Memorable.

Font styles to use
Serif
Sans Serif
Other font styles liked:
• verdana

Requirements
Must have
• card holders cell#, business phone#, fax#, email, website address, business address, logo
Nice to have
• use of medical/healthcare related descriptive words, items, look
Should not have
• the wrong colors or cartoon characters.

```html
<!DOCTYPE html>
<html lang="en">
<head>
<meta charset="utf-8">
<title>Stride DME – Business Card</title>
<link href="https://fonts.googleapis.com/css2?family=Source+Sans+3:wght@400;600;700&display=swap" rel="stylesheet">
<style>
  :root {
    --navy: #0f4a74;
    --green: #8cc63f;
    --teal: #1f8cc0;
    --ink: #1c4f7c;
    --white: #ffffff;
    --stage: #eceff2;
  }
  * { margin: 0; padding: 0; box-sizing: border-box; }
  html, body { width: 1200px; height: 1022px; overflow: hidden; }
  body {
    background: var(--stage);
    font-family: "Source Sans 3", Verdana, sans-serif;
    position: relative;
  }
  .card {
    position: absolute;
    left: 250px;
    width: 700px;
    height: 400px;
    background: var(--white);
    border-radius: 18px;
    overflow: hidden;
    box-shadow: 0 6px 22px rgba(0,0,0,.14);
  }
  .card--front { top: 50px; }
  .card--back { top: 552px; }

  .card__wave { position: absolute; inset: 0; }

  .brand {
    position: absolute;
    display: flex;
    flex-direction: column;
    align-items: flex-start;
    white-space: nowrap;
  }
  .card--front .brand { left: 250px; top: 26px; }
  .brand__name {
    display: flex; align-items: center; gap: 12px;
    color: var(--ink);
    font-weight: 600;
    font-size: 60px;
    line-height: 1;
    letter-spacing: -1px;
  }
  .brand__dot {
    width: 20px; height: 20px; border-radius: 50%;
    background: var(--green);
  }
  .brand__sub {
    margin-top: 6px;
    margin-left: 32px;
    color: var(--teal);
    font-weight: 600;
    font-size: 20px;
  }
  .tagline {
    position: absolute;
    color: var(--ink);
    font-size: 18px;
    line-height: 1.3;
  }
  .card--front .tagline { left: 462px; top: 140px; width: 220px; }

  .contact {
    position: absolute;
    left: 40px;
    top: 176px;
    color: var(--white);
    font-size: 17px;
    line-height: 1.22;
  }
  .contact__name {
    color: var(--green);
    font-weight: 700;
    font-size: 30px;
    line-height: 1.1;
  }
  .contact__row { display: flex; align-items: center; gap: 10px; }
  .contact__row svg { width: 13px; height: 13px; flex: none; }
  .contact__accent { color: var(--green); font-weight: 700; }

  .card--back .brand {
    left: 0; right: 0; top: 110px;
    align-items: center;
  }
  .card--back .brand__name { font-size: 76px; }
  .card--back .brand__sub { margin-left: 32px; font-size: 24px; }
  .card--back .tagline {
    left: 0; right: 0; top: 290px; text-align: center; font-size: 18px;
  }
</style>
</head>
<body>

<section class="card card--front">
  <svg class="card__wave" viewBox="0 0 700 400" preserveAspectRatio="none" aria-hidden="true">
    <path d="M0 110 C140 110 230 150 330 160 C430 170 480 190 520 400 L0 400 Z" fill="var(--green)"/>
    <path d="M0 128 C140 128 230 168 330 178 C420 187 462 210 498 400 L0 400 Z" fill="var(--navy)"/>
  </svg>

  <div class="brand">
    <div class="brand__name"><span class="brand__dot"></span>Stride DME</div>
    <div class="brand__sub">Durable Medical Equipment</div>
  </div>

  <p class="tagline">Medical equipment that gets you going and back in Stride</p>

  <div class="contact">
    <div class="contact__name">Marlon Hayes</div>
    <div>Director</div>
    <div>48 Harbor Lane Suite 210</div>
    <div>Lakeview, GA 30410</div>
    <div class="contact__row">
      <svg viewBox="0 0 14 14"><rect x="3" y="0.5" width="8" height="13" rx="1.5" fill="none" stroke="var(--green)" stroke-width="1.5"/></svg>+310 5182 4406</div>
    <div class="contact__row">
      <svg viewBox="0 0 14 14"><path d="M3 1 L5.5 1 L6.5 4 L5 5.5 C6 7.5 7 8.5 8.5 9 L10 7.5 L13 8.5 L13 11 C13 12 12 13 11 13 C6 12.5 1.5 8 1 3 C1 2 2 1 3 1Z" fill="var(--green)"/></svg>+310 5182 4471</div>
    <div class="contact__row">
      <svg viewBox="0 0 14 14"><rect x="1" y="5" width="12" height="8" rx="1" fill="var(--green)"/><rect x="3.5" y="1" width="7" height="4" fill="none" stroke="var(--green)" stroke-width="1.5"/></svg>+310 5182 4490</div>
    <div class="contact__row">
      <svg viewBox="0 0 14 14"><rect x="1" y="3" width="12" height="9" rx="1" fill="none" stroke="var(--green)" stroke-width="1.5"/><path d="M1.5 3.5 L7 8 L12.5 3.5" fill="none" stroke="var(--green)" stroke-width="1.5"/></svg>info@stridedme.com</div>
    <div class="contact__row">
      <svg viewBox="0 0 14 14"><circle cx="7" cy="7" r="6" fill="none" stroke="var(--green)" stroke-width="1.5"/><path d="M1 7 H13 M7 1 C4 4 4 10 7 13 M7 1 C10 4 10 10 7 13" fill="none" stroke="var(--green)" stroke-width="1.2"/></svg>www.<span class="contact__accent">stridedme</span>.com</div>
  </div>
</section>

<section class="card card--back">
  <div class="brand">
    <div class="brand__name"><span class="brand__dot"></span>Stride DME</div>
    <div class="brand__sub">Durable Medical Equipment</div>
  </div>
  <p class="tagline">Medical equipment that gets you going and back in Stride</p>
</section>

</body>
</html>
```